Web Design (Coded) and Project - Finance Company

Corvale Lending Group is a mortgage broker company based in Sydney Australia and provides lending solutions for individuals and businesses.

Our target market is anyone with the financial means to get a loan.

I am looking for a website design in this contest. The site needs to be able to be viewed on a portable device such as Tabra, Fonix, etc.

I have the logo design and files which need to be used. I also have the NLBC logo which will need to be in the footer of each page.

The website needs to represent a big finance company with integrity and knowledge.

The website will need to be uploaded to Hostwillow.example.au as they are the hosting provider. I will also need the ability to make changes to the text and pictures in the future and upload the revisions. I need the website ready to go and ready to be uploaded onto Host Willow.

The website will consist of 6 pages in total There are 4 main pages that will be viewed and then 2 with Privacy and Internal Dispute Resolution which are only accessed through links. These will be as follows:

Home
I would prefer to have a fresh bright and professional looking home page given that most mortgage broker websites look the same with the menu buttons at the top.

Services
Details the loan types that we handle and some text for each one.

About Us
I have the text for this.

Contact Us
Form to have the following inputs:
• Surname
• First Name
• Suburb
• State
• Phone number
• Mobile number
• Email address
• Preferred contact
o Phone
o Mobile
o Email
• Reason for Enquiry
o First home buyer
o Refinance
o Investment Property
o Commercial lending
o Personal loan
o Other
• Comments

Privacy
This page will only be accessed from a link at the bottom of each page. I have the wording that I will provide.

Dispute Resolution Policy
This page will only be accessed from a link on the Contact Us page. I have the wording that I will provide.
Updates

The designs that are coming through so far are generally looking the same generic website layout. I am looking for the home page to be something different with more of a wow factor and something different to the standard page link menu accross the top of the screen. The content should be fairly minimal given that I am a new business there will be limited text for each page. I am happy to increase the budget if required as I appreciate there will be more work involved.

Reason: I am extending the deadline as the design so far are good but fairly generic and template style home pages. For the home page I am looking for something a little more striking with a visual impact.

I have increased the payment by $200 to encourage more designs. Designs need to be relevant to the business, the number of pages and content. Several designs have come through looking good but just look like a standard template with my logo added, but the content does not match the business.

The brief stated that I am looking for the home page to be something different with more of a wow factor and something different to the standard page link menu accross the top of the screen. All of the designs have come through with the navigation bar along the top and a generic layout. I have attached a couple of idea's. Obviously these do not relate to the finance and mortgage industry but you can see the sort of style that gives the site a wow factor. The other pages can be more generic, but the first page is the attention grabber. You can also see the Fonix view that I am after. These are just templates from Host Willow that I could use to build the site, I just don't have the time or creative flair. Please submit more designs. Thanks for your work to date, Rob.

Hi. Could you please submit designs based on brief and the two screen shots attached. Mobile device view should work as per screen shots. Thanks, Rob

Reason: Still looking for designs to meet the brief provided.

Industry/Entity Type

Financial

Requirements
Must have
• Colour palette to be as supplied. I will post this shortly.
Should not have
• No cheesy smiley faces
No handshaking
No money pictures
No pictures of stones
No picture of people in an office looking at things
No lime green or purple in colour
Would prefer not to have a picture of the Quayline Span or Tidewater Hall

```html
<!DOCTYPE html>
<html lang="en">
<head>
<meta charset="utf-8">
<title>Corvale Lending Group</title>
<link href="https://fonts.googleapis.com/css2?family=Arimo:wght@400;700&display=swap" rel="stylesheet">
<style>
:root{
  --blue:#1a8fcf;
  --blue-dark:#0a6ea8;
  --blue-light:#5cc3ec;
  --orange:#f7931e;
  --orange-dark:#f07d00;
  --text:#333;
  --muted:#666;
  --grey:#8a8a8a;
  --line:#dcdcdc;
  --footer:#e6f3fa;
}
*{margin:0;padding:0;box-sizing:border-box}
html,body{width:1200px;height:948px;overflow:hidden;background:#fff;font-family:"Arimo",Arial,sans-serif;color:var(--text)}
.page{position:relative;width:1200px;height:948px}
.abs{position:absolute}
a{text-decoration:none;color:inherit}

.brand{left:248px;top:20px;display:flex;align-items:center;gap:10px}
.brand-mark{width:52px;height:52px;border-radius:50%;background:var(--blue)}
.brand-name{font-size:17px;font-weight:700;color:var(--blue-dark);line-height:1.1;width:110px}

.contact{right:468px;top:20px;text-align:right}
.contact .phone{font-size:29px;color:var(--blue);letter-spacing:.3px}
.contact .phone small{font-size:11px;vertical-align:top;margin-right:8px;position:relative;top:6px}
.contact .email{font-size:10px;font-weight:700;color:#444;margin-top:2px}

.hero{left:232px;top:86px;width:752px;height:320px;border-top:1px solid var(--line);border-left:1px solid var(--line);border-bottom:2px solid #d8d8d8}
.hero-panel{left:433px;top:86px;width:484px;height:305px;border-left:2px solid #e4e4e4;border-bottom:1px solid var(--line)}
.hero-title{left:469px;top:108px;font-size:50px;line-height:48px;font-weight:400;color:var(--orange)}
.hero-rule{left:472px;top:221px;width:83px;height:1px;background:var(--line)}
.hero-sub{left:471px;top:238px;font-size:22px;line-height:24px;color:#555}
.btn-orange{left:470px;top:337px;width:166px;height:28px;border-radius:14px;background:linear-gradient(#ffb21f,var(--orange-dark));color:#fff;font-size:10px;font-weight:700;padding:8px 15px;box-shadow:0 2px 3px rgba(0,0,0,.2)}
.btn-orange span{position:absolute;right:14px;top:7px}
.hero-photo{left:676px;top:96px;width:308px;height:284px;border-radius:40% 10% 0 40%;background:radial-gradient(circle at 55% 40%,#e8714a 0%,#f4d7c4 35%,#fff 72%)}
.slider-nav{left:934px;top:360px;width:66px;height:32px;background:#fff;border:1px solid var(--line);display:flex;box-shadow:0 1px 2px rgba(0,0,0,.1)}
.slider-nav span{flex:1;display:flex;align-items:center;justify-content:center;color:var(--blue-dark);font-size:12px;font-weight:700}
.slider-nav span+span{border-left:1px solid var(--line)}

.side-nav{left:215px;top:97px;width:200px;box-shadow:0 2px 4px rgba(0,0,0,.2)}
.side-nav a{display:flex;align-items:center;height:52px;padding-left:20px;gap:18px;color:#fff;font-size:12px;font-weight:700;background:linear-gradient(#43b5e4,#1e98d2);border-bottom:1px solid #127bb0;text-shadow:0 1px 1px rgba(0,0,0,.25)}
.side-nav a.active{background:linear-gradient(#b9e4f6,#86cfee)}
.side-nav svg{width:15px;height:15px;fill:#0d5f8d}
.side-note{left:248px;top:310px;width:167px;height:82px;background:linear-gradient(#fff,#eee);border:1px solid #ddd;padding:10px 10px 0 21px}
.side-note:before{content:"";position:absolute;left:9px;top:12px;width:2px;height:58px;background:var(--orange)}
.side-note h3{font-size:12px;font-weight:400;color:var(--blue-dark);margin-bottom:4px}
.side-note p{font-size:9.5px;line-height:14.4px;color:var(--text)}

.news-head{left:232px;top:420px;width:146px;height:142px;text-align:center;border-right:1px solid var(--line)}
.news-head h2{font-size:22px;font-weight:400;color:var(--orange);margin-top:48px}
.news-head svg{position:absolute;left:62px;top:14px;width:24px;height:24px}
.btn-grey{left:258px;top:515px;width:94px;height:24px;border-radius:12px;background:linear-gradient(#f7f7f7,#d9d9d9);font-size:10px;font-weight:700;color:#444;padding:6px 0 0 14px;box-shadow:0 1px 2px rgba(0,0,0,.2)}
.btn-grey span{position:absolute;right:12px;top:6px;color:#888}
.news-sep{left:681px;top:420px;width:1px;height:142px;background:var(--line)}
.news-item{width:190px}
.news-thumb{width:66px;height:64px}
.news-item .date{font-size:9px;color:var(--grey)}
.news-item h3{font-size:11px;color:var(--blue);font-weight:700;margin:2px 0 10px}
.news-item p{font-size:9.5px;line-height:14.4px;text-align:justify}
.news-item .more{display:block;margin-top:11px;font-size:10px;font-weight:700;color:var(--blue-dark)}
.news-item .more span{color:var(--grey);margin-left:6px}
.rule{left:232px;width:752px;height:1px;background:var(--line)}

.services-title{left:246px;top:576px;font-size:22px;font-weight:400;color:var(--orange)}
.service{width:220px;text-align:center}
.service-bg{position:absolute;left:-10px;top:-12px;width:240px;height:110px;background:radial-gradient(ellipse at center,#dbeef8 0%,#f1f8fc 50%,#fff 75%)}
.service-icon{position:relative;margin:0 auto;width:70px;height:70px;border-radius:50%;background:#fff;border:4px solid var(--blue);box-shadow:0 0 0 2px #9bd6f1,0 6px 8px rgba(0,0,0,.15);display:flex;align-items:center;justify-content:center}
.service-icon svg{width:36px;height:36px}
.service h3{position:relative;font-size:11px;color:var(--orange-dark);font-weight:700;margin-top:26px}
.service p{position:relative;font-size:9.5px;line-height:14.4px;text-align:justify;margin-top:10px}
.service p span{color:var(--orange);margin-left:4px}

.partners-label{left:246px;top:818px;font-size:14px;color:#777}
.partner{top:819px;font-size:15px;line-height:18px;color:#b5b5b5;display:flex;align-items:center;gap:7px;white-space:nowrap}
.partner i{display:block;width:16px;height:16px;background:#c9c9c9}
.partner i.round{border-radius:50%}

.footer{left:0;top:874px;width:1200px;height:74px;background:linear-gradient(#eef7fc,var(--footer));border-top:1px solid #d5e9f4}
.badge{left:246px;top:893px;width:92px;height:34px;border:2px solid #1b6fa8;background:linear-gradient(90deg,#fff 30%,#d4e9a8 30%,#b7d66b 100%)}
.foot-links{left:366px;top:896px;font-size:9px;font-weight:700;color:var(--blue);display:flex}
.foot-links a+a:before{content:"|";color:#bbb;font-weight:400;margin:0 10px}
.copyright{left:366px;top:915px;font-size:9px;font-weight:700;color:#666}
.back-top{left:909px;top:905px;font-size:9px;font-weight:700;color:#666}
.back-top span{color:var(--blue-light);margin-left:6px}
</style>
</head>
<body>
<div class="page">

  <div class="brand abs">
    <span class="brand-mark"></span>
    <span class="brand-name">Corvale Lending Group</span>
  </div>

  <div class="contact abs">
    <div class="phone"><small>+61</small>02 9000 1475</div>
    <div class="email">hello@corvalelending.example.au</div>
  </div>

  <div class="hero abs"></div>
  <div class="hero-panel abs"></div>
  <h1 class="hero-title abs">Mortgage<br>credit</h1>
  <div class="hero-rule abs"></div>
  <p class="hero-sub abs">Cras sollicitudin<br>metus et tortor<br>rutrum sed.</p>
  <a class="btn-orange abs" href="#">Read more<span>›</span></a>
  <div class="hero-photo abs" role="img" aria-label="Hand holding a small model house with a red tiled roof"></div>
  <div class="slider-nav abs"><span>‹</span><span>›</span></div>

  <nav class="side-nav abs">
    <a class="active" href="#"><svg viewBox="0 0 16 16"><path d="M8 1L0 8h2v7h4v-5h4v5h4V8h2z"/></svg>Home</a>
    <a href="#"><svg viewBox="0 0 16 16"><path d="M7 0h2l.4 2.2 1.6.7 1.9-1.3 1.4 1.4-1.3 1.9.7 1.6L16 7v2l-2.2.4-.7 1.6 1.3 1.9-1.4 1.4-1.9-1.3-1.6.7L9 16H7l-.4-2.2-1.6-.7-1.9 1.3-1.4-1.4 1.3-1.9-.7-1.6L0 9V7l2.2-.4.7-1.6-1.3-1.9 1.4-1.4 1.9 1.3 1.6-.7zM8 5a3 3 0 100 6 3 3 0 000-6z"/></svg>Services</a>
    <a href="#"><svg viewBox="0 0 16 16"><path d="M8 0a8 8 0 110 16A8 8 0 018 0zm-1 7v6h2V7zm0-3v2h2V4z"/></svg>About Us</a>
    <a href="#"><svg viewBox="0 0 16 16"><path d="M0 2h16v12H0zm1.5 1.5v.4L8 9l6.5-5.1v-.4zm0 2.3v6.7h13V5.8L8 11z"/></svg>Contact Us</a>
  </nav>

  <div class="side-note abs">
    <h3>Lorem ipsum</h3>
    <p>Donec id cursus tortor. Nullam eget ligula sed augue aliquet pharetra.</p>
  </div>

  <section class="news-head abs">
    <svg viewBox="0 0 24 24" fill="none" stroke="#555" stroke-width="2"><path d="M14 4H3v17h17V10"/><path d="M9 15l1-4 9-9 3 3-9 9z" fill="#555"/></svg>
    <h2>Latest news</h2>
  </section>
  <a class="btn-grey abs" href="#">View more<span>›</span></a>

  <article class="abs" style="left:394px;top:430px">
    <div class="news-thumb" role="img" aria-label="Business team meeting around a laptop" style="background:linear-gradient(135deg,#dfe3e8,#8a8f96 60%,#3a3d42)"></div>
  </article>
  <article class="news-item abs" style="left:473px;top:428px">
    <div class="date">10.12.2012, 12:35</div>
    <h3>Mauris vel velit eget lorem</h3>
    <p>Donec id cursus tortor. Nullam eget ligula sed augue aliquet pharetra. Aenean egestas vestibulum leo, eget fermentum odio dignissim interdum massa.</p>
    <a class="more" href="#">Read more<span>›</span></a>
  </article>

  <div class="news-sep abs"></div>

  <article class="abs" style="left:701px;top:430px">
    <div class="news-thumb" role="img" aria-label="Glass office towers against a blue sky" style="background:linear-gradient(160deg,#cfe6f7,#3d7fc0 55%,#173a66)"></div>
  </article>
  <article class="news-item abs" style="left:779px;top:428px">
    <div class="date">10.12.2012, 12:35</div>
    <h3>Cras eget lacus sem, eu gravida</h3>
    <p>Donec id cursus tortor. Nullam eget ligula sed augue aliquet pharetra. Aenean egestas vestibulum leo, eget fermentum odio dignissim tristique.</p>
    <a class="more" href="#">Read more<span>›</span></a>
  </article>

  <div class="rule abs" style="top:562px"></div>

  <h2 class="services-title abs">Our services</h2>

  <section class="service abs" style="left:256px;top:613px">
    <div class="service-bg" role="img" aria-label="Faint apartment buildings"></div>
    <div class="service-icon"><svg viewBox="0 0 36 36"><path d="M18 5L3 18h4v13h8v-8h6v8h8V18h4z" fill="var(--blue)"/></svg></div>
    <h3>Mortgage credit</h3>
    <p>Donec id cursus tortor. Nullam eget ligula sed augue aliquet pharetra. Aenean egestas vestibulum leo, eget fermentum odio dignissim.<span>›</span></p>
  </section>

  <section class="service abs" style="left:501px;top:613px">
    <div class="service-bg" role="img" aria-label="Faint financial documents"></div>
    <div class="service-icon"><svg viewBox="0 0 36 36"><text x="18" y="30" text-anchor="middle" font-family="Arimo,Arial,sans-serif" font-weight="700" font-size="30" fill="var(--blue)">$</text></svg></div>
    <h3>Cash credit</h3>
    <p>Quisque feugiat justo nec sapien feugiat vitae elementum massa sollicitudin. Fusce sodales dui vel risus vulputate adipiscing.<span>›</span></p>
  </section>

  <section class="service abs" style="left:745px;top:613px">
    <div class="service-bg" role="img" aria-label="Faint charts and reports"></div>
    <div class="service-icon"><svg viewBox="0 0 36 36" fill="var(--blue)"><rect x="5" y="25" width="5" height="6"/><rect x="12" y="21" width="5" height="10"/><rect x="19" y="23" width="5" height="8"/><rect x="26" y="17" width="5" height="14"/><path d="M4 19l9-8 6 5 8-8-3-2h9v9l-2-3-12 12-6-5-8 7z"/></svg></div>
    <h3>Investment</h3>
    <p>Donec id cursus tortor. Nullam eget ligula sed augue aliquet pharetra. Aenean egestas vestibulum leo, eget fermentum odio dignissim.<span>›</span></p>
  </section>

  <div class="rule abs" style="top:787px"></div>

  <div class="partners-label abs">Our partners</div>
  <div class="partner abs" style="left:362px">Norvik Bank</div>
  <div class="partner abs" style="left:530px"><i class="round"></i>Valmont Credit</div>
  <div class="partner abs" style="left:700px"><i></i>Halden Trust</div>
  <div class="partner abs" style="left:848px">Marisol Bank</div>

  <footer class="footer abs"></footer>
  <div class="badge abs" role="img" aria-label="NLBC approved broker badge"></div>
  <nav class="foot-links abs">
    <a href="#">Home</a><a href="#">Services</a><a href="#">About Us</a><a href="#">Contact Us</a><a href="#">Privacy</a>
  </nav>
  <div class="copyright abs">Copyright 2012 Corvale Lending Group. All Right Reserved.</div>
  <a class="back-top abs" href="#">Back to top<span>˄</span></a>

</div>
</body>
</html>
```